Creative label for amber glass candle jar.

We are a candle company. Our products are handmade by us and natural. We are looking for something minimalistic and unique. We need a label for our candle jars (amber glass with black lid). Our current label doesn't match these requirements. We would like our products to be stocked in London shop, therefore design has to be up to a high standard. Jar specification Diameter (mm) 65 Height without cap (mm) 80. We want the new design to be different from the current one. It's just a guide for wording.
We should be able adjust the label, to change scent name.
Our scents are
*Coconut & Vanilla
*Lavender
*Bergamot
*Italian Garden
*Hygge
*Eucalyptus & Peppermint
*Coffee
*Cedarwood & Juniperberry
To know more about us, visit our website www.wrenfieldcandles.com or instagram.com/wrenfieldcandles
Good luck!
Industry/Entity Type
It Company
Colors
Designer to choose colors to be used in the design.
Requirements
Must have
- * I have attached two of our logos, label design must include one of them.
- *has to mention that it's made in London
- *has to say that candle is natural/made with essential oils
- *has to have scent name and No. on it..
- Label can be vertical or horizontal, but has to be square/rectangular,.
Should not have
- Label should not be round

```html
<!DOCTYPE html>
<html lang="en">
<head>
<meta charset="utf-8">
<title>Wrenfield Candle Labels</title>
<link rel="stylesheet" href="https://fonts.googleapis.com/css2?family=Barlow+Condensed:wght@300;400;500;600&family=Barlow:wght@300&display=swap">
<style>
  :root {
    --backdrop: #323232;
    --paper: #ffffff;
    --ink: #231f20;
    --band: #8b898a;
  }
  * { margin: 0; padding: 0; box-sizing: border-box; }
  html, body { width: 1200px; height: 640px; overflow: hidden; background: var(--backdrop); }
  body { -webkit-font-smoothing: antialiased; -moz-osx-font-smoothing: grayscale; }
  .sheet { position: relative; width: 1200px; height: 640px; }

  .label {
    position: absolute;
    background: var(--paper);
    color: var(--ink);
    font-family: "Barlow Condensed", sans-serif;
    overflow: hidden;
  }
  .label > * { position: absolute; }
  .label__line { left: 0; right: 0; text-align: center; line-height: 1.15; white-space: nowrap; }

  .side-block { background: var(--ink); }
  .side-band { background: var(--band); }

  .brand-mark {
    border-radius: 50%;
    background: var(--ink);
    color: var(--paper);
    display: flex; align-items: center; justify-content: center;
    font-family: "Barlow", sans-serif; font-weight: 300;
  }
  .scent-name { font-weight: 600; }
  .scent-note { font-weight: 500; }
  .claim { font-weight: 300; }
  .origin { font-weight: 600; }
  .label__number { font-weight: 500; line-height: 1; }

  /* Large label */
  .label--large { width: 440px; height: 440px; }
  .label--large .side-block--top { left: 0; top: 0; width: 26px; height: 52px; }
  .label--large .side-band--left { left: 0; top: 56px; width: 26px; height: 330px; }
  .label--large .side-band--right { right: 0; top: 52px; width: 26px; height: 334px; }
  .label--large .side-block--bottom { right: 0; top: 386px; width: 26px; height: 54px; }
  .label--large .label__number { left: 42px; top: 16px; font-size: 29px; }
  .label--large .brand-mark { left: 146px; top: 34px; width: 149px; height: 149px; font-size: 33px; letter-spacing: 2px; }
  .label--large .scent-name { top: 214px; font-size: 32px; letter-spacing: 3px; }
  .label--large .scent-note { top: 260px; font-size: 18px; letter-spacing: 7px; }
  .label--large .divider { left: 70px; top: 303px; width: 300px; height: 4px; }
  .label--large .claim { top: 328px; font-size: 17px; letter-spacing: 0.3px; }
  .label--large .origin { top: 366px; font-size: 12px; letter-spacing: 1.6px; }
  .label--large .flag { left: 200px; top: 400px; width: 40px; height: 20px; }

  /* Small labels */
  .label--small { width: 197px; height: 197px; }
  .label--small .side-block--top { left: 0; top: 0; width: 12px; height: 23px; }
  .label--small .side-band--left { left: 0; top: 25px; width: 12px; height: 148px; }
  .label--small .side-band--right { right: 0; top: 23px; width: 12px; height: 150px; }
  .label--small .side-block--bottom { right: 0; top: 173px; width: 12px; height: 24px; }
  .label--small .label__number { left: 19px; top: 9px; font-size: 12.5px; }
  .label--small .brand-mark { left: 65px; top: 16px; width: 67px; height: 67px; font-size: 15px; letter-spacing: 1px; }
  .label--small .scent-name { top: 95px; font-size: 13px; letter-spacing: 0.8px; }
  .label--small .scent-name--long { font-size: 12.5px; letter-spacing: 0; }
  .label--small .scent-note { top: 116px; font-size: 7.5px; letter-spacing: 2.2px; }
  .label--small .scent-note--long { letter-spacing: 1.8px; }
  .label--small .divider { left: 31px; top: 135px; width: 135px; height: 2px; }
  .label--small .claim { top: 146px; font-size: 7px; }
  .label--small .origin { top: 162px; font-size: 5px; letter-spacing: 0.6px; }
  .label--small .flag { left: 92px; top: 178px; width: 14px; height: 7px; }
</style>
</head>
<body>
<svg width="0" height="0" style="position:absolute" aria-hidden="true">
  <defs>
    <symbol id="rule" viewBox="0 0 300 4" preserveAspectRatio="none">
      <path d="M0 2 Q150 -0.5 300 2 Q150 4.5 0 2 Z" fill="#231f20"/>
    </symbol>
    <symbol id="uk-flag" viewBox="0 0 60 30">
      <rect width="60" height="30" fill="#231f20"/>
      <path d="M0 0 L60 30 M60 0 L0 30" stroke="#fff" stroke-width="6"/>
      <path d="M0 0 L60 30 M60 0 L0 30" stroke="#231f20" stroke-width="2"/>
      <path d="M30 0 V30 M0 15 H60" stroke="#fff" stroke-width="10"/>
      <path d="M30 0 V30 M0 15 H60" stroke="#231f20" stroke-width="6"/>
    </symbol>
  </defs>
</svg>

<main class="sheet">
  <article class="label label--large" style="left:35px; top:104px;">
    <div class="side-block side-block--top"></div>
    <div class="side-band side-band--left" role="img" aria-label="Striped side band with chevron motif"></div>
    <div class="side-band side-band--right" role="img" aria-label="Striped side band with chevron motif"></div>
    <div class="side-block side-block--bottom"></div>
    <p class="label__number">№ 01</p>
    <div class="brand-mark">wrenfield</div>
    <h2 class="label__line scent-name">LAVENDER</h2>
    <p class="label__line scent-note">COMFORT &amp; RELAXATION</p>
    <svg class="divider" aria-hidden="true"><use href="#rule"/></svg>
    <p class="label__line claim">Natural and made with essential oils</p>
    <p class="label__line origin">MADE IN LONDON</p>
    <svg class="flag" role="img" aria-label="Union flag"><use href="#uk-flag"/></svg>
  </article>

  <article class="label label--small" style="left:509px; top:104px;">
    <div class="side-block side-block--top"></div>
    <div class="side-band side-band--left" role="img" aria-label="Striped side band with chevron motif"></div>
    <div class="side-band side-band--right" role="img" aria-label="Striped side band with chevron motif"></div>
    <div class="side-block side-block--bottom"></div>
    <p class="label__number">№02</p>
    <div class="brand-mark">wrenfield</div>
    <h2 class="label__line scent-name">BERGAMOT</h2>
    <p class="label__line scent-note scent-note--long">WITH AROMATIC ELEMENTS</p>
    <svg class="divider" aria-hidden="true"><use href="#rule"/></svg>
    <p class="label__line claim">Natural and made with essential oils</p>
    <p class="label__line origin">MADE IN LONDON</p>
    <svg class="flag" role="img" aria-label="Union flag"><use href="#uk-flag"/></svg>
  </article>

  <article class="label label--small" style="left:737px; top:104px;">
    <div class="side-block side-block--top"></div>
    <div class="side-band side-band--left" role="img" aria-label="Striped side band with chevron motif"></div>
    <div class="side-band side-band--right" role="img" aria-label="Striped side band with chevron motif"></div>
    <div class="side-block side-block--bottom"></div>
    <p class="label__number">№03</p>
    <div class="brand-mark">wrenfield</div>
    <h2 class="label__line scent-name">ITALIAN GARDEN</h2>
    <p class="label__line scent-note">MEMORY BOOSTER</p>
    <svg class="divider" aria-hidden="true"><use href="#rule"/></svg>
    <p class="label__line claim">Natural and made with essential oils</p>
    <p class="label__line origin">MADE IN LONDON</p>
    <svg class="flag" role="img" aria-label="Union flag"><use href="#uk-flag"/></svg>
  </article>

  <article class="label label--small" style="left:966px; top:104px;">
    <div class="side-block side-block--top"></div>
    <div class="side-band side-band--left" role="img" aria-label="Striped side band with chevron motif"></div>
    <div class="side-band side-band--right" role="img" aria-label="Striped side band with chevron motif"></div>
    <div class="side-block side-block--bottom"></div>
    <p class="label__number">№04</p>
    <div class="brand-mark">wrenfield</div>
    <h2 class="label__line scent-name">HYGGE</h2>
    <p class="label__line scent-note scent-note--long">HEARTWARMING COMBINATION</p>
    <svg class="divider" aria-hidden="true"><use href="#rule"/></svg>
    <p class="label__line claim">Natural and made with essential oils</p>
    <p class="label__line origin">MADE IN LONDON</p>
    <svg class="flag" role="img" aria-label="Union flag"><use href="#uk-flag"/></svg>
  </article>

  <article class="label label--small" style="left:509px; top:346px;">
    <div class="side-block side-block--top"></div>
    <div class="side-band side-band--left" role="img" aria-label="Striped side band with chevron motif"></div>
    <div class="side-band side-band--right" role="img" aria-label="Striped side band with chevron motif"></div>
    <div class="side-block side-block--bottom"></div>
    <p class="label__number">№05</p>
    <div class="brand-mark">wrenfield</div>
    <h2 class="label__line scent-name scent-name--long">EUCALYPTUS &amp; PEPPERMINT</h2>
    <p class="label__line scent-note">REFRESHING &amp; MINTY</p>
    <svg class="divider" aria-hidden="true"><use href="#rule"/></svg>
    <p class="label__line claim">Natural and made with essential oils</p>
    <p class="label__line origin">MADE IN LONDON</p>
    <svg class="flag" role="img" aria-label="Union flag"><use href="#uk-flag"/></svg>
  </article>

  <article class="label label--small" style="left:737px; top:346px;">
    <div class="side-block side-block--top"></div>
    <div class="side-band side-band--left" role="img" aria-label="Striped side band with chevron motif"></div>
    <div class="side-band side-band--right" role="img" aria-label="Striped side band with chevron motif"></div>
    <div class="side-block side-block--bottom"></div>
    <p class="label__number">№06</p>
    <div class="brand-mark">wrenfield</div>
    <h2 class="label__line scent-name">COFFEE</h2>
    <p class="label__line scent-note">ALLURING AROMA</p>
    <svg class="divider" aria-hidden="true"><use href="#rule"/></svg>
    <p class="label__line claim">Natural and made with essential oils</p>
    <p class="label__line origin">MADE IN LONDON</p>
    <svg class="flag" role="img" aria-label="Union flag"><use href="#uk-flag"/></svg>
  </article>

  <article class="label label--small" style="left:966px; top:346px;">
    <div class="side-block side-block--top"></div>
    <div class="side-band side-band--left" role="img" aria-label="Striped side band with chevron motif"></div>
    <div class="side-band side-band--right" role="img" aria-label="Striped side band with chevron motif"></div>
    <div class="side-block side-block--bottom"></div>
    <p class="label__number">№07</p>
    <div class="brand-mark">wrenfield</div>
    <h2 class="label__line scent-name scent-name--long">CEDARWOOD &amp; JUNIPERBERRY</h2>
    <p class="label__line scent-note">RELAXING</p>
    <svg class="divider" aria-hidden="true"><use href="#rule"/></svg>
    <p class="label__line claim">Natural and made with essential oils</p>
    <p class="label__line origin">MADE IN LONDON</p>
    <svg class="flag" role="img" aria-label="Union flag"><use href="#uk-flag"/></svg>
  </article>
</main>
</body>
</html>
```